Elegant wordpress web page for wedding rental of hand sanitizers

We want to rent our hand sanitizing towers out for high-end weddings. We need a very elegant, sophisticated page that describes our offering. You can see an ugly first draft here: purvant.com/weddings
Target Market(s)
Wedding planners, wedding parents
Number of Pages Required
1 page
Font styles to use
Serif
Script
Colors
Designer to choose colors to be used in the design.
Requirements
Nice to have
- Two wedding-related sites for inspiration: lacetrellisweddings-dot-com and fennoreventservices-dot-com

```html
<!DOCTYPE html>
<html lang="en">
<head>
<meta charset="utf-8">
<title>Purvant — Personalized Hand Sanitizer Towers for Weddings</title>
<link rel="stylesheet" href="https://fonts.googleapis.com/css2?family=Great+Vibes&family=Poppins:wght@400;500;600;700&display=swap">
<style>
:root{
  --ink:#2b2b2b;
  --muted:#6d6d6d;
  --brand:#1c5f91;
  --brand-deep:#155a8a;
  --accent:#1e96d6;
  --btn-grey:#e7e7e7;
  --soft-bg:#f5f5f5;
  --line:#d9d9d9;
  --white:#ffffff;
}
*{box-sizing:border-box;margin:0;padding:0}
html,body{width:1200px;height:4827px;overflow:hidden}
body{position:relative;font-family:"Poppins",sans-serif;color:var(--ink);background:var(--white)}
.abs{position:absolute}
.script{font-family:"Great Vibes",cursive;color:var(--brand);font-weight:400;line-height:1}
.eyebrow{font-size:13px;font-weight:600;color:var(--brand);text-transform:uppercase;line-height:20px}
.wave{display:block;margin-top:12px}
.body-copy{font-size:13px;color:var(--muted);line-height:23px}
.bullets{list-style:none}
.bullets li{position:relative;padding-left:22px;font-size:13px;color:var(--muted);line-height:23px;margin-top:14px}
.bullets li::before{content:"";position:absolute;left:2px;top:7px;width:9px;height:9px;border-radius:50%;border:2px solid #cfcfcf}
.btn-check{display:inline-block;background:var(--btn-grey);font-size:11px;font-weight:600;color:#333;text-transform:uppercase;padding:0 22px;height:40px;line-height:40px;letter-spacing:.2px}
.media{border-radius:4px}

/* header */
.site-header{left:0;top:0;width:1200px;height:100px;background:var(--white)}
.brand-name{font-weight:600;color:var(--brand);font-size:40px;line-height:1}
.main-nav{left:457px;top:38px;display:flex;gap:22px;font-size:13px;font-weight:500;color:#333;text-transform:uppercase}
.search{left:872px;top:28px;width:238px;height:40px;background:#f1f1f1;border-radius:3px;font-size:12px;color:#999;padding-left:16px;line-height:40px}
.search svg{position:absolute;right:12px;top:11px}

/* hero */
.hero{left:0;top:100px;width:1200px;height:612px;background:linear-gradient(160deg,#8c6d5a 0%,#b79f8d 40%,#7a6255 100%)}
.hero-title{left:565px;top:215px;font-size:140px;color:var(--white)}
.hero-sub{left:571px;top:345px;font-size:30px;font-weight:600;color:var(--white);text-transform:uppercase}
.hero-text{left:571px;top:395px;width:380px;font-size:16px;color:var(--white);line-height:23px}
.btn-shop{left:570px;top:467px;width:135px;height:41px;background:var(--accent);color:var(--white);font-size:12px;font-weight:600;display:flex;align-items:center;justify-content:center;gap:10px}

/* portfolio */
.gallery-tile{top:3428px;height:307px}

/* testimonials */
.avatar{border-radius:50%;background:#c9b7ad}
.quote{left:240px;top:4160px;width:720px;text-align:center;font-size:19px;line-height:31px;color:#555}
.arrow-btn{width:60px;height:60px;border-radius:50%;background:#ececec;display:flex;align-items:center;justify-content:center}

/* footer */
.site-footer{left:0;top:4434px;width:1200px;height:393px;background:var(--brand-deep);color:var(--white)}
.footer-nav{left:0;top:4620px;width:1200px;display:flex;justify-content:center;gap:28px;font-size:13px;font-weight:500;text-transform:uppercase}
.social{width:42px;height:42px;border-radius:50%;background:rgba(255,255,255,.18);top:4657px}
.footer-rule{left:88px;top:4759px;width:1024px;height:1px;background:rgba(255,255,255,.3)}
.copyright{left:0;top:4786px;width:1200px;text-align:center;font-size:13px}
.legal{right:90px;top:4786px;font-size:13px}
.to-top{left:1145px;top:4745px;width:34px;height:34px;border-radius:50%;background:var(--accent);display:flex;align-items:center;justify-content:center}
</style>
</head>
<body>

<header class="abs site-header">
  <div class="abs brand-name" style="left:88px;top:28px">purvant</div>
  <nav class="abs main-nav"><span>About</span><span>Products</span><span>Industry Solutions</span><span>Contact</span></nav>
  <div class="abs search">Search here...
    <svg width="18" height="18" viewBox="0 0 18 18" fill="none" stroke="#777" stroke-width="1.6"><circle cx="7.5" cy="7.5" r="5.5"/><path d="M11.5 11.5L16 16"/></svg>
  </div>
</header>

<section class="abs hero" role="img" aria-label="Blurred wedding reception hall background"></section>
<svg class="abs" style="left:0;top:560px" width="1200" height="152" viewBox="0 0 1200 152"><path d="M0 90 C200 40 350 120 560 80 C760 40 900 110 1200 60 L1200 152 L0 152Z" fill="#fff" opacity=".25"/><path d="M0 120 C250 80 450 140 700 110 C900 90 1050 130 1200 100 L1200 152 L0 152Z" fill="#fff" opacity=".35"/></svg>
<div class="abs media" style="left:131px;top:184px;width:300px;height:696px;background:linear-gradient(180deg,#c9b1a6 0%,#8e4b4a 45%,#f2f2f2 65%,#d8d8d8 100%)" role="img" aria-label="Hand sanitizer tower topped with a wedding couple photo"></div>
<div class="abs script hero-title">Personalize</div>
<div class="abs hero-sub">Your Hand Sanitizer</div>
<p class="abs hero-text">We want to rent our hand sanitizing towers out for high-end weddings.</p>
<div class="abs btn-shop">SHOP NOW <svg width="16" height="10" viewBox="0 0 16 10" fill="none" stroke="#fff" stroke-width="1.5"><path d="M0 5H14M10 1l4 4-4 4"/></svg></div>

<!-- welcome -->
<section class="abs" style="left:88px;top:920px;width:460px">
  <h2 class="script" style="font-size:72px">Welcome</h2>
  <p class="eyebrow" style="margin-top:8px">Your guests with something truly unique a<br>customized hand sanitizer</p>
  <svg class="wave" width="48" height="8" viewBox="0 0 48 8" fill="none" stroke="#ccc" stroke-width="1.5"><path d="M0 4q6-6 12 0t12 0 12 0 12 0"/></svg>
  <p class="body-copy" style="margin-top:10px">Why have a generic, industrial hand sanitizer when you could have something truly unique and different?</p>
  <ul class="bullets">
    <li>Customize the photo above the spout and the spout decoration</li>
    <li>Choose any size and shape photo you wish</li>
    <li>Choose from our standard spout decorations or design one of your own.&nbsp; We'll take care of producing and fitting it.</li>
  </ul>
</section>
<div class="abs btn-check" style="left:88px;top:1277px">Check price and availability</div>
<div class="abs" style="left:572px;top:859px;width:553px;height:547px;background:radial-gradient(circle,#e8e2de 0%,#b9a6a6 55%,#fff 75%)" role="img" aria-label="Sanitizer tower photo framed by a gold geometric frame and pastel flowers"></div>

<!-- customize -->
<div class="abs" style="left:178px;top:1453px;width:385px;height:507px;background:radial-gradient(ellipse at 50% 70%,#f0c7b8 0%,#e9ecea 45%,#fff 75%)" role="img" aria-label="Three personalized sanitizer towers with watercolor flowers"></div>
<section class="abs" style="left:660px;top:1505px;width:420px">
  <h2 class="script" style="font-size:72px">Customize</h2>
  <p class="eyebrow" style="margin-top:16px">Your sanitizer with any photo,<br>any size, any shape</p>
  <svg class="wave" width="48" height="8" viewBox="0 0 48 8" fill="none" stroke="#ccc" stroke-width="1.5"><path d="M0 4q6-6 12 0t12 0 12 0 12 0"/></svg>
  <ul class="bullets">
    <li>Choose a photo of the happy couple, the proud parents, or anything else you wish</li>
    <li>Choose any size or shape you wish, up to 24x36"</li>
    <li>We take care of all production and customization</li>
  </ul>
</section>
<div class="abs btn-check" style="left:660px;top:1817px">Check price and availability</div>

<!-- choose -->
<section class="abs" style="left:0;top:2012px;width:1200px;height:716px;background:linear-gradient(180deg,var(--soft-bg),#fff)"></section>
<section class="abs" style="left:88px;top:2185px;width:420px">
  <h2 class="script" style="font-size:72px">Choose</h2>
  <p class="eyebrow" style="margin-top:12px">One of our standard spouts, or<br>design your own</p>
  <svg class="wave" width="48" height="8" viewBox="0 0 48 8" fill="none" stroke="#ccc" stroke-width="1.5"><path d="M0 4q6-6 12 0t12 0 12 0 12 0"/></svg>
  <ul class="bullets">
    <li>Choose one of our standard spouts - wedding cake, flower vase, or "just married" car.&nbsp; More spout decorations will be added each month</li>
    <li>For an additional fee, our team of 3D designers will design, 3D print, and decorate a spout just for your event</li>
  </ul>
</section>
<div class="abs btn-check" style="left:88px;top:2514px">Check price and availability</div>
<div class="abs" style="left:544px;top:2091px;width:544px;height:609px;background:radial-gradient(ellipse,#f3dcd8 0%,#f6c7c6 45%,rgba(255,255,255,0) 72%)" role="img" aria-label="Pink and green paper flowers behind the photo"></div>
<div class="abs" style="left:597px;top:2172px;width:360px;height:414px;background:#fff;box-shadow:0 6px 18px rgba(0,0,0,.15)"></div>
<div class="abs" style="left:605px;top:2180px;width:344px;height:398px;background:linear-gradient(160deg,#e9e5df,#cfc6bb 60%,#ebe7e2)" role="img" aria-label="Sanitizer tower beside a white wedding arch decorated with roses"></div>

<!-- greet -->
<div class="abs" style="left:141px;top:2766px;width:459px;height:459px;background:radial-gradient(ellipse at 45% 60%,#f3b8a3 0%,#e7eedd 45%,#fff 72%)" role="img" aria-label="Sanitizer tower with a bouquet of peach watercolor roses"></div>
<section class="abs" style="left:660px;top:2805px;width:420px">
  <h2 class="script" style="font-size:72px">Greet</h2>
  <p class="eyebrow" style="margin-top:12px">Your guests with an act of care</p>
  <svg class="wave" width="48" height="8" viewBox="0 0 48 8" fill="none" stroke="#ccc" stroke-width="1.5"><path d="M0 4q6-6 12 0t12 0 12 0 12 0"/></svg>
  <ul class="bullets">
    <li>Make your friends and family feel welcome and safe with a rugged, durable hand sanitizer from Purvant</li>
    <li>Our battery-powered dispensers are reliable, wireless, and touchless</li>
    <li>Filled with your choice from our wide range of sanitizing products</li>
  </ul>
</section>
<div class="abs btn-check" style="left:660px;top:3112px">Check price and availability</div>

<!-- portfolio -->
<h2 class="abs script" style="left:0;top:3300px;width:1200px;text-align:center;font-size:76px">Our Portfolio</h2>
<svg class="abs" style="left:576px;top:3385px" width="48" height="8" viewBox="0 0 48 8" fill="none" stroke="#ccc" stroke-width="1.5"><path d="M0 4q6-6 12 0t12 0 12 0 12 0"/></svg>
<div class="abs gallery-tile" style="left:0;width:146px;background:linear-gradient(135deg,#6b4a3a,#d7cfc8)" role="img" aria-label="Sanitizer tower at a rustic venue"></div>
<div class="abs gallery-tile" style="left:150px;width:281px;background:linear-gradient(135deg,#e0ddd8,#b8a8a0 50%,#f1f0ee)" role="img" aria-label="Sanitizer tower with couple photo in a white hallway"></div>
<div class="abs gallery-tile" style="left:446px;width:308px;background:linear-gradient(135deg,#5f7a4b,#e8e2dc 55%,#d8cfc8)" role="img" aria-label="Sanitizer tower at an outdoor tent reception"></div>
<div class="abs gallery-tile" style="left:767px;width:279px;background:linear-gradient(135deg,#f2f2f2,#c9c2bb 60%,#eeeeee)" role="img" aria-label="Row of sanitizer towers in a bright room"></div>
<div class="abs gallery-tile" style="left:1050px;width:150px;background:linear-gradient(135deg,#8a7a5f,#c9b6aa)" role="img" aria-label="Sanitizer tower in a garden ceremony"></div>

<!-- testimonials -->
<h2 class="abs script" style="left:0;top:3818px;width:1200px;text-align:center;font-size:76px">Testimonials</h2>
<svg class="abs" style="left:576px;top:3900px" width="48" height="8" viewBox="0 0 48 8" fill="none" stroke="#ccc" stroke-width="1.5"><path d="M0 4q6-6 12 0t12 0 12 0 12 0"/></svg>
<div class="abs avatar" style="left:212px;top:3960px;width:56px;height:56px" role="img" aria-label="Client portrait"></div>
<div class="abs avatar" style="left:392px;top:3960px;width:56px;height:56px;background:#a9968a" role="img" aria-label="Client portrait"></div>
<div class="abs avatar" style="left:552px;top:3932px;width:96px;height:96px;background:#b9aaa0" role="img" aria-label="Portrait of Marcus Ellery"></div>
<div class="abs avatar" style="left:752px;top:3960px;width:56px;height:56px;background:#9b8478" role="img" aria-label="Client portrait"></div>
<div class="abs avatar" style="left:932px;top:3960px;width:56px;height:56px;background:#bdb3ac" role="img" aria-label="Client portrait"></div>
<div class="abs" style="left:150px;top:4055px;width:900px;height:2px;background:var(--line)"></div>
<div class="abs" style="left:0;top:4088px;width:1200px;text-align:center;font-size:16px;font-weight:600;color:#222">MARCUS ELLERY</div>
<div class="abs" style="left:0;top:4114px;width:1200px;text-align:center;font-size:11px;color:#888">ADVISOR</div>
<p class="abs quote">Fashion should be nominated for service of the year. I will refer everyone I know. I would like to personally thank you for your outstanding product. Not able to tell you how happy I am with fashion</p>
<div class="abs arrow-btn" style="left:534px;top:4271px"><svg width="20" height="12" viewBox="0 0 20 12" fill="none" stroke="#333" stroke-width="1.5"><path d="M20 6H2M6 1L1 6l5 5"/></svg></div>
<div class="abs arrow-btn" style="left:604px;top:4271px"><svg width="20" height="12" viewBox="0 0 20 12" fill="none" stroke="#333" stroke-width="1.5"><path d="M0 6h18M14 1l5 5-5 5"/></svg></div>
<div class="abs" style="left:919px;top:4247px;width:281px;height:187px;background:radial-gradient(ellipse at 60% 70%,#f0a38c 0%,#b7cfe6 40%,rgba(255,255,255,0) 72%)" role="img" aria-label="Bouquet of colorful paper flowers"></div>

<!-- footer -->
<footer class="abs site-footer"></footer>
<div class="abs brand-name" style="left:0;top:4506px;width:1200px;text-align:center;color:var(--white);font-size:76px">purvant</div>
<nav class="abs footer-nav"><span>Home</span><span>About us</span><span>Our products</span><span>Industry solutions</span><span>Contact us</span></nav>
<div class="abs social" style="left:527px"></div>
<div class="abs social" style="left:579px"></div>
<div class="abs social" style="left:630px"></div>
<div class="abs footer-rule"></div>
<div class="abs copyright">© Copyright 2021 PURVANT, LLC&nbsp; All Rights Reserved</div>
<div class="abs legal">Sitemap &nbsp;•&nbsp; Privacy Policy</div>
<div class="abs to-top"><svg width="12" height="12" viewBox="0 0 12 12" fill="none" stroke="#fff" stroke-width="1.5"><path d="M6 12V1M2 5l4-4 4 4"/></svg></div>

</body>
</html>
```